Software as a Service to manage Home Care Management

We need a web site designed for Home Care Management Software as a Service product, that facilitates Home Care organizations to manage and schedule carers to visit client homes. We want a modern look and feel using our existing logo.

Target Market(s)

Home Care Management organizations. Product is similar to: https://wovenpath.co/

Coding

Coded - Design and coding required

Number of Pages Required

3 page

```html
<!DOCTYPE html>
<html lang="en">
<head>
<meta charset="utf-8">
<title>HomeShift — Home Care Management</title>
<link rel="stylesheet" href="https://fonts.googleapis.com/css2?family=Lora:wght@400;500;700&family=Open+Sans:wght@400;600&display=swap">
<style>
  :root {
    --pink: #f5437f;
    --pink-soft: #f7679a;
    --ink: #1b1b1b;
    --dark: #262626;
    --grey-panel: #f3f3f3;
    --grey-band: #ececec;
    --text: #444;
    --muted: #777;
    --white: #fff;
    --line: #cfcfcf;
  }
  * { box-sizing: border-box; margin: 0; padding: 0; }
  html, body { width: 1200px; height: 3434px; overflow: hidden; }
  body { position: relative; background: var(--white); font-family: "Open Sans", Arial, sans-serif; color: var(--text); }
  .serif { font-family: "Lora", Georgia, serif; }
  .section { position: absolute; left: 0; width: 1200px; }
  .btn { display: inline-flex; align-items: center; justify-content: center; font-family: "Lora", Georgia, serif; font-size: 16px; color: var(--white); background: var(--pink); text-transform: uppercase; text-decoration: none; border-radius: 2px; }
  .rule { width: 80px; height: 4px; background: var(--pink); }
  .placeholder { position: absolute; }

  /* header */
  .site-header { top: 0; height: 69px; background: var(--white); }
  .brand { position: absolute; left: 144px; top: 18px; display: flex; align-items: center; gap: 10px; font-family: "Lora", Georgia, serif; font-size: 23px; color: var(--dark); }
  .brand-dot { width: 30px; height: 30px; border-radius: 50%; background: var(--pink); }
  .nav { position: absolute; left: 420px; top: 26px; display: flex; font-family: "Lora", Georgia, serif; font-size: 14px; color: var(--dark); }
  .nav a { color: inherit; text-decoration: none; position: absolute; white-space: nowrap; }
  .nav a.active { color: var(--pink); }
  .header-cta { position: absolute; left: 936px; top: 17px; width: 120px; height: 36px; font-size: 14px; }

  /* hero */
  .hero { top: 69px; height: 546px; }
  .hero-photo { left: 0; top: 0; width: 672px; height: 546px; background: linear-gradient(120deg, #e9e6e4 0%, #d9cfca 45%, #c8b8ae 100%); }
  .hero-panel { position: absolute; left: 672px; top: 0; width: 528px; height: 546px; background: linear-gradient(180deg, #f7589a 0%, #f4548f 100%); }
  .hero-copy { position: absolute; right: 144px; top: 133px; width: 360px; text-align: right; color: var(--white); }
  .hero-copy h1 { font-family: "Lora", Georgia, serif; font-weight: 500; font-size: 29px; line-height: 37px; }
  .hero-copy p { margin-top: 14px; font-size: 16px; line-height: 27px; color: #ffe4ee; }
  .hero-actions { margin-top: 18px; display: flex; justify-content: flex-end; gap: 8px; }
  .hero-actions .btn { background: var(--dark); height: 47px; padding: 0 19px; text-transform: uppercase; }
  .dots { position: absolute; right: 144px; top: 392px; display: flex; gap: 20px; }
  .dots span { width: 12px; height: 12px; border-radius: 50%; background: var(--dark); }
  .dots span:first-child { background: var(--white); }

  /* features */
  .features { top: 615px; height: 506px; }
  .section-title { text-align: center; font-family: "Lora", Georgia, serif; font-weight: 500; font-size: 34px; color: var(--ink); }
  .features .section-title { margin-top: 73px; }
  .features .rule { margin: 18px auto 0; }
  .feature-grid { position: absolute; left: 144px; top: 166px; width: 912px; display: flex; gap: 20px; }
  .feature { width: 291px; text-align: center; }
  .feature-icon { width: 160px; height: 160px; margin: 0 auto; border-radius: 50%; background: var(--pink); display: flex; align-items: center; justify-content: center; }
  .feature h3 { margin-top: 14px; font-family: "Lora", Georgia, serif; font-weight: 500; font-size: 25px; color: var(--ink); }
  .feature p { margin-top: 8px; font-size: 11.5px; line-height: 21px; color: var(--text); }

  /* dark intro */
  .intro { top: 1121px; height: 536px; }
  .intro-panel { position: absolute; left: 0; top: 0; width: 600px; height: 536px; background: var(--dark); color: #ddd; }
  .intro-panel h2 { position: absolute; left: 144px; top: 64px; font-family: "Lora", Georgia, serif; font-weight: 500; font-size: 34px; color: var(--white); }
  .intro-panel .rule { position: absolute; left: 144px; top: 133px; }
  .intro-text { position: absolute; left: 144px; top: 160px; width: 422px; font-size: 11.5px; line-height: 25.6px; color: #d8d8d8; }
  .intro-text p + p { margin-top: 25px; }
  .intro-panel .btn { position: absolute; left: 145px; top: 415px; width: 160px; height: 48px; }
  .intro-photo { left: 600px; top: 0; width: 600px; height: 536px; background: linear-gradient(110deg, #ecebec 0%, #e3dfe2 55%, #d8cdd3 100%); }

  /* checklist */
  .benefits { top: 1741px; height: 436px; }
  .benefits-photo { left: 144px; top: 0; width: 456px; height: 436px; background: linear-gradient(135deg, #e6e0d8 0%, #cfc6bb 50%, #b9ada2 100%); }
  .benefits-panel { position: absolute; left: 600px; top: 0; width: 456px; height: 436px; background: var(--grey-panel); }
  .benefits-panel h2 { position: absolute; left: 38px; top: 18px; font-family: "Lora", Georgia, serif; font-weight: 500; font-size: 32px; color: var(--ink); }
  .benefits-panel .rule { position: absolute; left: 38px; top: 82px; }
  .checklist { position: absolute; left: 38px; top: 110px; list-style: none; }
  .checklist li { display: flex; align-items: center; gap: 10px; height: 33.5px; font-size: 15px; color: var(--text); }
  .benefits-panel .btn { position: absolute; left: 39px; top: 367px; width: 136px; height: 47px; }

  /* testimonials */
  .testimonials { top: 2264px; height: 436px; }
  .testimonial-panel { position: absolute; left: 144px; top: 0; width: 456px; height: 436px; background: var(--grey-panel); }
  .testimonial-panel h2 { position: absolute; left: 24px; top: 16px; font-family: "Lora", Georgia, serif; font-weight: 500; font-size: 34px; color: var(--ink); }
  .testimonial-panel .rule { position: absolute; left: 24px; top: 82px; }
  .quote { position: absolute; left: 24px; top: 109px; width: 420px; font-size: 19px; line-height: 36.5px; color: #3a3a3a; }
  .quote .mark { color: var(--pink); font-family: "Lora", Georgia, serif; font-weight: 700; font-size: 26px; line-height: 1; }
  .quote-author { position: absolute; left: 24px; top: 308px; font-family: "Lora", Georgia, serif; font-size: 25px; color: #3a3a3a; }
  .testimonial-panel .btn { position: absolute; left: 25px; top: 367px; width: 136px; height: 47px; }
  .testimonial-photo { left: 600px; top: 0; width: 456px; height: 436px; background: linear-gradient(135deg, #cbbfae 0%, #9c8c7a 55%, #6f6356 100%); }

  /* contact */
  .contact { top: 2773px; height: 550px; background: var(--grey-band); }
  .contact .section-title { margin-top: 76px; }
  .contact .rule { margin: 18px auto 0; }
  .contact-form { position: absolute; left: 144px; top: 166px; width: 912px; }
  .field-row { display: flex; gap: 10px; margin-bottom: 19px; }
  .field { flex: 1; height: 38px; background: var(--white); border: 1px solid var(--line); font-size: 12.5px; color: var(--muted); padding: 10px 15px; position: relative; }
  .field.message { height: 127px; }
  .field .caret { position: absolute; right: 14px; top: 15px; }
  .contact .submit { position: absolute; left: 532px; top: 3195px; }
  .submit-btn { position: absolute; left: 388px; top: 256px; width: 136px; height: 47px; }

  /* footer */
  .site-footer { top: 3323px; height: 111px; background: var(--dark); color: #d5d5d5; font-size: 11.5px; }
  .footer-links { position: absolute; left: 144px; top: 30px; display: flex; gap: 8px; }
  .footer-links span.sep { color: #999; }
  .copyright { position: absolute; left: 144px; top: 64px; }
  .social { position: absolute; left: 990px; top: 43px; display: flex; gap: 22px; }
  .social span { width: 22px; height: 22px; border-radius: 50%; background: #d5d5d5; }
</style>
</head>
<body>

<header class="section site-header">
  <div class="brand"><span class="brand-dot"></span>HomeShift</div>
  <nav class="nav">
    <a class="active" style="left:0">PRODUCT</a>
    <a style="left:96px">PRICING</a>
    <a style="left:183px">BLOG</a>
    <a style="left:251px">FAQ</a>
    <a style="left:309px">ABOUT US</a>
    <a style="left:408px">CONTACT US</a>
  </nav>
  <a class="btn header-cta">Book a Demo</a>
</header>

<section class="section hero">
  <div class="placeholder hero-photo" role="img" aria-label="Photo of a smiling carer supporting an elderly woman at home"></div>
  <div class="hero-panel">
    <div class="hero-copy">
      <h1>Etiam massa elementum bibendum tellus venenatis</h1>
      <p>Pellentesque convallis molestie enim sit amet efficitur. Etiam id imperdiet lectus. Vivamus lacus justo ultrices nec erat.</p>
      <div class="hero-actions">
        <a class="btn">Log In</a>
        <a class="btn">How It Works</a>
      </div>
    </div>
    <div class="dots"><span></span><span></span><span></span><span></span></div>
  </div>
</section>

<section class="section features">
  <h2 class="section-title">Aliquam erat volutpat</h2>
  <div class="rule"></div>
  <div class="feature-grid">
    <div class="feature">
      <div class="feature-icon">
        <svg width="70" height="70" viewBox="0 0 70 70" fill="none" stroke="#fff" stroke-width="3" stroke-linejoin="round">
          <path d="M10 34 L35 12 L60 34"/><path d="M18 28 V60 H52 V28"/><path d="M30 60 V44 H40 V60"/>
        </svg>
      </div>
      <h3>FUSCE EGET</h3>
      <p>Vivamus lacus justo, ultrices nec erat in, euismod iaculis mauris. Vivamus eleifend vitae nulla vel malesuada. In ac malesuada.</p>
    </div>
    <div class="feature">
      <div class="feature-icon">
        <svg width="70" height="80" viewBox="0 0 70 80" fill="none" stroke="#fff" stroke-width="3">
          <rect x="14" y="4" width="42" height="72" rx="6"/><line x1="28" y1="12" x2="42" y2="12"/><circle cx="35" cy="66" r="2.5" fill="#fff"/><line x1="30" y1="44" x2="44" y2="22"/><line x1="36" y1="48" x2="46" y2="32"/>
        </svg>
      </div>
      <h3>ETIAM QUIS</h3>
      <p>Vivamus lacus justo, ultrices nec erat in, euismod iaculis mauris. Vivamus eleifend vitae nulla vel malesuada. In ac malesuada.</p>
    </div>
    <div class="feature">
      <div class="feature-icon">
        <svg width="80" height="70" viewBox="0 0 80 70" fill="none" stroke="#fff" stroke-width="3" stroke-linejoin="round">
          <path d="M40 62 C22 48 8 38 8 22 C8 12 16 6 25 6 C32 6 37 10 40 16 C43 10 48 6 55 6 C64 6 72 12 72 22 C72 38 58 48 40 62 Z"/>
        </svg>
      </div>
      <h3>DUIS ORNARE</h3>
      <p>Vivamus lacus justo, ultrices nec erat in, euismod iaculis mauris. Vivamus eleifend vitae nulla vel malesuada. In ac malesuada.</p>
    </div>
  </div>
</section>

<section class="section intro">
  <div class="intro-panel">
    <h2>Cras sollicitudin</h2>
    <div class="rule"></div>
    <div class="intro-text">
      <p>Vivamus lacus justo, ultrices nec erat in, euismod iaculis mauris. Vivamus eleifend vitae nulla vel malesuada. In ac malesuada lacus, et consectetur ante. Fusce vitae lectus sit amet mi pulvinar maximus. Aenean placerat, nibh vel accumsan aliquet, magna nibh accumsan nibh, ac tempus nunc ipsum ac tellus.</p>
      <p>Vestibulum ante ipsum primis in faucibus orci luctus et ultrices posuere cubilia Curae; Vestibulum eget nisl metus. Phasellus nisl est, condimentum vitae faucibus in, sollicitudin vel metus. Nunc sit amet consequat risus. Curabitur ac elit leo. In eleifend dui tellus, in scelerisque elit porttitor et.</p>
    </div>
    <a class="btn">Book a Demo</a>
  </div>
  <div class="placeholder intro-photo" role="img" aria-label="Photo of a hand holding a smartphone showing the app login screen"></div>
</section>

<section class="section benefits">
  <div class="placeholder benefits-photo" role="img" aria-label="Photo of a smiling elderly woman using a tablet on a sofa"></div>
  <div class="benefits-panel">
    <h2>Phasellus blandit quam</h2>
    <div class="rule"></div>
    <ul class="checklist">
      <li><svg width="13" height="13" viewBox="0 0 13 13"><circle cx="6.5" cy="6.5" r="6.5" fill="#f5437f"/><path d="M3.6 6.7 L5.6 8.6 L9.4 4.6" stroke="#fff" stroke-width="1.6" fill="none"/></svg>Donec quis ex semper consequat ligula</li>
      <li><svg width="13" height="13" viewBox="0 0 13 13"><circle cx="6.5" cy="6.5" r="6.5" fill="#f5437f"/><path d="M3.6 6.7 L5.6 8.6 L9.4 4.6" stroke="#fff" stroke-width="1.6" fill="none"/></svg>Aliquam malesuada eros sit amet turpis scelerisque</li>
      <li><svg width="13" height="13" viewBox="0 0 13 13"><circle cx="6.5" cy="6.5" r="6.5" fill="#f5437f"/><path d="M3.6 6.7 L5.6 8.6 L9.4 4.6" stroke="#fff" stroke-width="1.6" fill="none"/></svg>Maecenas lobortis iaculis efficitur</li>
      <li><svg width="13" height="13" viewBox="0 0 13 13"><circle cx="6.5" cy="6.5" r="6.5" fill="#f5437f"/><path d="M3.6 6.7 L5.6 8.6 L9.4 4.6" stroke="#fff" stroke-width="1.6" fill="none"/></svg>Vestibulum pharetra diam</li>
      <li><svg width="13" height="13" viewBox="0 0 13 13"><circle cx="6.5" cy="6.5" r="6.5" fill="#f5437f"/><path d="M3.6 6.7 L5.6 8.6 L9.4 4.6" stroke="#fff" stroke-width="1.6" fill="none"/></svg>Praesent accumsan nunc a condimentum</li>
      <li><svg width="13" height="13" viewBox="0 0 13 13"><circle cx="6.5" cy="6.5" r="6.5" fill="#f5437f"/><path d="M3.6 6.7 L5.6 8.6 L9.4 4.6" stroke="#fff" stroke-width="1.6" fill="none"/></svg>Sed quis metus nibh</li>
      <li><svg width="13" height="13" viewBox="0 0 13 13"><circle cx="6.5" cy="6.5" r="6.5" fill="#f5437f"/><path d="M3.6 6.7 L5.6 8.6 L9.4 4.6" stroke="#fff" stroke-width="1.6" fill="none"/></svg>Phasellus congue dapibus sapien eu tincidunt</li>
    </ul>
    <a class="btn">Read More</a>
  </div>
</section>

<section class="section testimonials">
  <div class="testimonial-panel">
    <h2>Testimonials</h2>
    <div class="rule"></div>
    <p class="quote"><span class="mark">“</span>&nbsp; Vestibulum id scelerisque turpis, vulputate neque. Mauris molestie vitae condimentum. Curabitur eu erat dignissim, varius ipsum non, dictum turpis. Vestibulum convallis rutrum tin cidunt velit consectetur. &nbsp;<span class="mark">”</span></p>
    <p class="quote-author">- Mara Ellis, City</p>
    <a class="btn">View All</a>
  </div>
  <div class="placeholder testimonial-photo" role="img" aria-label="Portrait photo of a smiling elderly man holding a walking cane"></div>
</section>

<section class="section contact">
  <h2 class="section-title">Contact Us</h2>
  <div class="rule"></div>
  <form class="contact-form">
    <div class="field-row">
      <div class="field">First name</div>
      <div class="field">Last name</div>
      <div class="field">Email</div>
    </div>
    <div class="field-row">
      <div class="field">Phone Number</div>
      <div class="field">Demo Date</div>
      <div class="field">Time<svg class="caret" width="12" height="7" viewBox="0 0 12 7"><path d="M0 0 H12 L6 7 Z" fill="#555"/></svg></div>
    </div>
    <div class="field-row">
      <div class="field message">Message</div>
    </div>
    <a class="btn submit-btn">Submit</a>
  </form>
</section>

<footer class="section site-footer">
  <div class="footer-links">
    <span>Home</span><span class="sep">|</span><span>Product</span><span class="sep">|</span><span>Pricing</span><span class="sep">|</span><span>Blog</span><span class="sep">|</span><span>FAQ</span><span class="sep">|</span><span>About Us</span><span class="sep">|</span><span>Contact Us</span><span class="sep">|</span><span>Book a Demo</span>
  </div>
  <p class="copyright">Copyright © 2020 &nbsp;HomeShift. &nbsp;All rights reserved.</p>
  <div class="social"><span></span><span></span></div>
</footer>

</body>
</html>
```